Business Card for a Wellness and Aesthetic Center

I'd like to have a business card design for a Wellness and Aesthetic Center based in the Philippines called "Tidelark Wellness and Aesthetic Inc." They provide services such as medical and aesthetic dermatology. Specializing on cosmetic and anti-aging procedures.

The target market of the business is mostly women from the upper class from 30 to 60 years old.

The feel and look of the card should be feminine, modern, minimalist and classy.

The colors to play with are gold and black.

The front part should contain:
- Name (example: Marisol Tebenay Quiroga, MD)
- Designation (example: Medical Director)
- Company Logo

The back part should contain:
- Company Logo
- Address
- Contact Details
- Website

For more details and inspiration you may visit their website at http://tidelarkph.com/

Thank you very much!

Target Market(s)

Women from the upper class from 30 to 60 years old.

Industry/Entity Type

Business

Contact Information for Business Card

- Company Logo

- Company Logo
- Address
- Contact Details
- Website

Font styles to use
Serif
Script

Colors
ffc214
fece3e
faa54b
f78f20
000000

Requirements
Must have
• Design should be feminine, modern, minimalist/simple and classy.
Nice to have
• You can play with lines, curves, gardient and be creative on the placement of texts and logo.
Should not have
• Pictures like body, face or nature scene.

```html
<!DOCTYPE html>
<html lang="en">
<head>
<meta charset="utf-8">
<title>Tidelark Wellness and Aesthetic Inc. — Business Card</title>
<link rel="stylesheet" href="https://fonts.googleapis.com/css2?family=Source+Sans+3:wght@400;600&display=swap">
<style>
  :root {
    --stage: #e8ebec;
    --white: #ffffff;
    --black: #000000;
    --ink: #1a1a1a;
    --gold: #ffc214;
    --gold-soft: #fece3e;
    --amber: #faa54b;
    --orange: #f78f20;
    --logo-gold: #e39a1c;
    --pattern-dark: #0d0d0d;
    --pattern-mid: #1e1e1e;
    --contact-text: #e6e6e6;
  }
  * { box-sizing: border-box; margin: 0; padding: 0; }
  html, body { width: 1200px; height: 900px; overflow: hidden; }
  body {
    background: var(--stage);
    font-family: "Source Sans 3", "Segoe UI", sans-serif;
    display: flex;
    flex-direction: column;
    align-items: center;
    justify-content: center;
    gap: 50px;
  }
  .card {
    width: 760px;
    height: 380px;
    position: relative;
    overflow: hidden;
    box-shadow: 0 6px 18px rgba(0,0,0,0.12);
  }

  /* Front */
  .card-front { display: flex; }
  .front-logo-panel {
    width: 46%;
    background: var(--white);
    display: flex;
    align-items: center;
    justify-content: center;
  }
  .logo-disc {
    width: 260px;
    height: 260px;
    border-radius: 50%;
    background: var(--black);
    display: flex;
    align-items: center;
    justify-content: center;
  }
  .wordmark {
    color: var(--logo-gold);
    font-weight: 400;
    font-size: 40px;
    letter-spacing: 0.02em;
  }
  .front-name-panel {
    flex: 1;
    background: linear-gradient(135deg, var(--gold) 0%, var(--amber) 55%, var(--gold) 100%);
    display: flex;
    flex-direction: column;
    justify-content: center;
    padding: 0 40px;
  }
  .person-name {
    color: var(--ink);
    font-weight: 600;
    font-size: 26px;
    line-height: 1.2;
  }
  .person-title {
    color: var(--white);
    font-size: 18px;
    margin-top: 6px;
    align-self: flex-end;
    margin-right: 10px;
  }

  /* Back */
  .card-back { background: var(--black); }
  .damask-field {
    position: absolute;
    inset: 0;
    background: radial-gradient(ellipse at 40% 45%, var(--pattern-mid) 0%, var(--pattern-dark) 70%);
  }
  .back-logo {
    position: absolute;
    left: 70px;
    top: 50%;
    transform: translateY(-50%);
    font-size: 52px;
  }
  .contact-list {
    position: absolute;
    right: 60px;
    top: 50%;
    transform: translateY(-50%);
    list-style: none;
    display: flex;
    flex-direction: column;
    gap: 12px;
    color: var(--contact-text);
    font-size: 16px;
    letter-spacing: 0.03em;
  }
  .contact-item { display: flex; align-items: flex-start; gap: 12px; }
  .contact-icon { width: 16px; height: 16px; flex: none; margin-top: 2px; fill: var(--gold); }
  .address-lines { line-height: 1.35; }
</style>
</head>
<body>

  <section class="card card-front" aria-label="Business card front">
    <div class="front-logo-panel">
      <div class="logo-disc">
        <span class="wordmark">Tidelark</span>
      </div>
    </div>
    <div class="front-name-panel">
      <p class="person-name">Marisol Tebenay Quiroga, MD</p>
      <p class="person-title">Medical Director</p>
    </div>
  </section>

  <section class="card card-back" aria-label="Business card back">
    <div class="damask-field" role="img" aria-label="Dark black damask floral pattern background"></div>
    <span class="wordmark back-logo">Tidelark</span>
    <ul class="contact-list">
      <li class="contact-item">
        <svg class="contact-icon" viewBox="0 0 16 16" aria-hidden="true"><path d="M8 1a5 5 0 0 0-5 5c0 3.8 5 9 5 9s5-5.2 5-9a5 5 0 0 0-5-5zm0 7a2 2 0 1 1 0-4 2 2 0 0 1 0 4z"/></svg>
        <span class="address-lines">Basement, Harbor Crest Tower<br>Calderon Business Park<br>Solano, Marivel City, PH</span>
      </li>
      <li class="contact-item">
        <svg class="contact-icon" viewBox="0 0 16 16" aria-hidden="true"><path d="M4 1l2.5 3.5-1.5 1.5c.8 2 2.5 3.7 4.5 4.5l1.5-1.5L15 12l-1.5 2.5C8 15 1 8 1.5 2.5z"/></svg>
        <span>(632) 555-0148</span>
      </li>
      <li class="contact-item">
        <svg class="contact-icon" viewBox="0 0 16 16" aria-hidden="true"><path d="M1 3h14v10H1zm1.5 1.5v.3L8 8.5l5.5-3.7v-.3zm0 2v5h11v-5L8 10.2z"/></svg>
        <span>beauty@tidelarkph.com</span>
      </li>
      <li class="contact-item">
        <svg class="contact-icon" viewBox="0 0 16 16" aria-hidden="true"><path d="M8 1a7 7 0 1 0 0 14A7 7 0 0 0 8 1zm0 1.5c.7 0 1.6 1.6 1.9 4H6.1c.3-2.4 1.2-4 1.9-4zm-2 .5a9 9 0 0 0-1.4 3.5H2.7A5.6 5.6 0 0 1 6 3zm4 0a5.6 5.6 0 0 1 3.3 3.5h-1.9A9 9 0 0 0 10 3zM2.7 8h1.9A9 9 0 0 0 6 13 5.6 5.6 0 0 1 2.7 8zm3.4 0h3.8c-.3 2.4-1.2 4-1.9 4s-1.6-1.6-1.9-4zm5.3 0h1.9A5.6 5.6 0 0 1 10 13a9 9 0 0 0 1.4-5z"/></svg>
        <span>www.tidelarkph.com</span>
      </li>
    </ul>
  </section>

</body>
</html>
```